Training Certificate of Completion

This certificate should be an A4 page size, please make this landscape. Please visit our website www.velmorcoaching.com.au to see our design & colour style.

Please include:
- Course Name
- Certificate Stamp (Personalised, no ribbons)
- Student Name
- Completion date
- Room for head trainers signature
- 9 digit student id number
- OKU learnings address & website
Updates

Reason: We require a certificate with actual design features, not just a boarder.

Target Market(s)

Professional engineers

Industry/Entity Type

Landscape

Requirements
Must have
• Design elements are essential, we need something more then a pretty boarder.
Should not have
• Ribbons on the Certificate Seal

```html
<!DOCTYPE html>
<html lang="en">
<head>
<meta charset="utf-8">
<title>Certificate of Training</title>
<link rel="stylesheet" href="https://fonts.googleapis.com/css2?family=UnifrakturMaguntia&family=Great+Vibes&family=Cormorant+Garamond:wght@500;700&family=Arimo:wght@400;700&family=Herr+Von+Muellerhoff&display=swap">
<style>
:root{
  --ink:#111111;
  --label-red:#e8112d;
  --frame-blue:#1c1ccf;
  --title-navy:#141a7a;
  --paper:#fbf8ee;
  --page:#ffffff;
  --rule:#9a9a9a;
  --ornament-fill:#d9d9d9;
  --seal-fill:#e4e2f4;
}
*{box-sizing:border-box;margin:0;padding:0}
html,body{width:1200px;height:1000px;overflow:hidden;background:var(--page)}
.canvas{position:relative;width:1200px;height:1000px}
.corner-option{position:absolute;background:var(--ornament-fill)}
.option-b1{left:104px;top:82px;width:150px;height:150px}
.option-b2{left:305px;top:82px;width:224px;height:210px}
.option-b3{left:603px;top:78px;width:214px;height:214px}
.option-b4{left:888px;top:78px;width:224px;height:214px}
.option-label{position:absolute;font-family:"Arimo",sans-serif;font-weight:700;font-size:46px;line-height:1;color:var(--label-red)}
.label-b1{left:104px;top:262px}
.label-b2{left:390px;top:180px}
.label-b3{left:685px;top:200px}
.label-b4{left:972px;top:200px}
.certificate{position:absolute;left:200px;top:370px;width:800px;height:580px;background:var(--paper);
  box-shadow:0 4px 14px rgba(0,0,0,.25);color:var(--ink);text-align:center}
.frame{position:absolute;inset:0}
.brand{position:absolute;top:48px;left:0;right:0;display:flex;justify-content:center;align-items:center;gap:10px}
.brand-dot{width:34px;height:34px;border-radius:50%;background:var(--title-navy)}
.brand-name{font-family:"Arimo",sans-serif;font-weight:700;font-size:28px;color:var(--title-navy);letter-spacing:1px}
.title{position:absolute;top:80px;left:0;width:800px;height:140px}
.title text{font-family:"UnifrakturMaguntia",serif;font-size:62px;fill:var(--title-navy)}
.caps{font-family:"Cormorant Garamond",serif;font-weight:500;font-size:19px;letter-spacing:.5px;text-transform:uppercase;line-height:1.1}
.awarded{position:absolute;top:212px;left:0;right:0}
.recipient{position:absolute;top:238px;left:0;right:0;font-family:"Great Vibes",cursive;font-size:52px}
.completion{position:absolute;top:310px;left:0;right:0}
.course{position:absolute;top:360px;left:0;right:0;font-family:"Cormorant Garamond",serif;font-weight:700;font-size:24px}
.given{position:absolute;top:390px;left:0;right:0;font-size:17px}
.signature-block{position:absolute;left:100px;top:428px;width:220px}
.signature{font-family:"Herr Von Muellerhoff",cursive;font-size:40px;line-height:1;text-align:left}
.signature-line{border-top:1px solid var(--rule);margin-top:2px;padding-top:4px;font-size:16px}
.student-id{position:absolute;left:92px;top:506px;font-family:"Cormorant Garamond",serif;font-weight:700;font-size:18px;text-transform:uppercase}
.student-id span{font-size:22px;letter-spacing:1.5px}
.seal{position:absolute;left:352px;top:436px;width:76px;height:76px;border-radius:50%;
  background:var(--seal-fill);border:3px double var(--frame-blue)}
.issuer{position:absolute;right:110px;top:470px;font-family:"Arimo",sans-serif;text-align:center}
.issuer-name{font-weight:700;font-size:19px}
.issuer-detail{font-size:14px;line-height:1.2}
</style>
</head>
<body>
<main class="canvas">
  <div class="corner-option option-b1" role="img" aria-label="Border corner ornament option B-1"></div>
  <div class="corner-option option-b2" role="img" aria-label="Border corner ornament option B-2"></div>
  <div class="corner-option option-b3" role="img" aria-label="Border corner ornament option B-3"></div>
  <div class="corner-option option-b4" role="img" aria-label="Border corner ornament option B-4"></div>
  <p class="option-label label-b1">B-1</p>
  <p class="option-label label-b2">B-2</p>
  <p class="option-label label-b3">B-3</p>
  <p class="option-label label-b4">B-4</p>

  <section class="certificate">
    <svg class="frame" viewBox="0 0 800 580" aria-hidden="true">
      <rect x="24" y="24" width="752" height="532" fill="none" stroke="var(--frame-blue)" stroke-width="1.5"/>
      <g fill="var(--frame-blue)">
        <rect x="18" y="18" width="10" height="10"/><rect x="772" y="18" width="10" height="10"/>
        <rect x="18" y="552" width="10" height="10"/><rect x="772" y="552" width="10" height="10"/>
      </g>
    </svg>

    <div class="brand"><span class="brand-dot"></span><span class="brand-name">OKU LEARNING</span></div>

    <svg class="title" viewBox="0 0 800 140" aria-label="Certificate of Training">
      <path id="title-arc" d="M120 110Q400 60 680 120" fill="none"/>
      <text text-anchor="middle"><textPath href="#title-arc" startOffset="50%">Certificate of Training</textPath></text>
    </svg>

    <p class="caps awarded">This certificate is awarded to</p>
    <p class="recipient">Daniel R. Hart</p>
    <p class="caps completion">For having successfully completed and fulfilled<br>the requirements of the course for</p>
    <p class="course">COURSE NAME/DESCRIPTION</p>
    <p class="caps given">Given at New York, USA<br>June 20, 2015</p>

    <div class="signature-block">
      <p class="signature">Signature</p>
      <p class="caps signature-line">Training Instructor</p>
    </div>
    <p class="student-id">Student ID No.: <span>123-4567-89</span></p>

    <div class="seal" role="img" aria-label="Personalised certificate stamp"></div>

    <div class="issuer">
      <p class="issuer-name">OKU LEARNING COMPANY</p>
      <p class="issuer-detail">New Tork City, USA<br>www.okulearningcenter.com</p>
    </div>
  </section>
</main>
</body>
</html>
```